Business Card Design Project

We need a buisness card for a new digital sinage company. Our target cliants are small to mediaum buisness who want to advertise on out digital sinage network

Target Market(s)

Small to medium buisness

Industry/Entity Type

Digital

Requirements
Must have
• Must have logo

```html
<!DOCTYPE html>
<html lang="en">
<head>
<meta charset="utf-8">
<title>Vizo business cards</title>
<link rel="stylesheet" href="https://fonts.googleapis.com/css2?family=Arimo:wght@400;700&display=swap">
<style>
  :root {
    --canvas-bg: #e4e4e2;
    --card-white: #ffffff;
    --ink: #111111;
    --text-grey: #333333;
    --brand-blue: #1b5fae;
    --blue-light: #1f9ce0;
    --blue-dark: #0f55a8;
    --green-light: #8cc63f;
    --green-dark: #157a1c;
    --mark-blue: #1a73c7;
    --divider: #9a9a9a;
  }
  * { box-sizing: border-box; margin: 0; padding: 0; }
  html, body { width: 1200px; height: 722px; overflow: hidden; }
  body {
    background: var(--canvas-bg);
    font-family: "Arimo", Arial, sans-serif;
    position: relative;
  }
  .card {
    position: absolute;
    width: 526px;
    height: 301px;
    box-shadow: 0 3px 8px rgba(0,0,0,0.35);
    overflow: hidden;
  }
  .card--front { left: 58px; top: 48px; background: var(--card-white); }
  .card--back-white { left: 614px; top: 48px; background: var(--card-white); }
  .card--back-blue { left: 60px; top: 374px; background: linear-gradient(90deg, var(--blue-light), var(--blue-dark)); }
  .card--back-green { left: 614px; top: 374px; background: linear-gradient(90deg, var(--green-light), var(--green-dark)); }

  .brand { position: absolute; display: flex; align-items: center; gap: 16px; }
  .brand__square { background: var(--mark-blue); display: block; }
  .brand__name { font-weight: 700; color: var(--ink); letter-spacing: -1px; line-height: 1; }

  .card--front .brand { left: 58px; top: 108px; }
  .card--front .brand__square { width: 64px; height: 64px; }
  .card--front .brand__name { font-size: 50px; }

  .divider { position: absolute; left: 302px; top: 92px; width: 1px; height: 100px;
    background: linear-gradient(180deg, transparent, var(--divider) 30%, var(--divider) 70%, transparent); }
  .contact { position: absolute; left: 322px; top: 95px; }
  .contact__name { color: var(--brand-blue); font-size: 16px; font-weight: 700; margin-bottom: 17px; }
  .contact__list { list-style: none; }
  .contact__item { display: flex; align-items: center; gap: 7px; font-size: 13px; color: var(--text-grey); height: 19px; }
  .contact__item svg { width: 10px; height: 10px; fill: var(--brand-blue); }

  .swoosh { position: absolute; left: 0; top: 0; width: 526px; height: 301px; }
  .address { position: absolute; left: 64px; top: 270px; color: #fff; font-size: 13px; }

  .brand--centered { left: 50%; transform: translateX(-50%); }
  .card--back-white .brand { top: 132px; }
  .card--back-white .brand__square { width: 60px; height: 60px; }
  .card--back-white .brand__name { font-size: 48px; }

  .card--back-blue .brand { top: 120px; gap: 22px; }
  .card--back-blue .brand__square { width: 92px; height: 92px; background: #ffffff; opacity: 0.9; }
  .card--back-blue .brand__square { background: var(--mark-blue); box-shadow: inset 0 0 0 2px rgba(255,255,255,0.5); }
  .card--back-blue .brand__name { font-size: 66px; }

  .card--back-green .brand { top: 90px; }
  .card--back-green .brand__square { width: 72px; height: 72px; background: #ffffff; }
  .card--back-green .brand__name { font-size: 48px; color: #ffffff; }

  .url { position: absolute; left: 0; right: 0; text-align: center; font-size: 14px; letter-spacing: 3px; }
  .card--back-white .url { top: 213px; color: var(--text-grey); }
  .card--back-white .url__domain { color: var(--blue-dark); }
  .card--back-blue .url { top: 252px; color: #ffffff; }
  .card--back-green .url { top: 218px; color: #ffffff; }
</style>
</head>
<body>
  <section class="card card--front" aria-label="Card front">
    <div class="brand">
      <span class="brand__square"></span>
      <span class="brand__name">Vizo</span>
    </div>
    <div class="divider"></div>
    <div class="contact">
      <p class="contact__name">Marcus Ellery</p>
      <ul class="contact__list">
        <li class="contact__item">
          <svg viewBox="0 0 10 10"><path d="M2 0.5 L3.6 2.8 L2.7 3.8 Q4 6.2 6.2 7.3 L7.2 6.4 L9.5 8 L8.3 9.5 Q1 8 0.5 1.7 Z"/></svg>
          0400 512 738
        </li>
        <li class="contact__item">
          <svg viewBox="0 0 10 10"><path d="M0.5 2 H9.5 V8.5 H0.5 Z M1.2 2.6 L5 5.6 L8.8 2.6" stroke="#fff" stroke-width="0.8"/></svg>
          marcus@vizo.com.au
        </li>
        <li class="contact__item">
          <svg viewBox="0 0 10 10"><circle cx="5" cy="5" r="4.5"/><path d="M0.5 5 H9.5 M5 0.5 V9.5 M5 0.5 Q2 5 5 9.5 M5 0.5 Q8 5 5 9.5" stroke="#fff" stroke-width="0.6" fill="none"/></svg>
          www.vizo.com.au
        </li>
      </ul>
    </div>
    <svg class="swoosh" viewBox="0 0 526 301" aria-hidden="true">
      <defs>
        <linearGradient id="band-blue" x1="0" x2="1" y1="0" y2="0">
          <stop offset="0" stop-color="#1f9ce0"/>
          <stop offset="1" stop-color="#0f55a8"/>
        </linearGradient>
        <linearGradient id="band-green" x1="0" x2="1" y1="0" y2="0">
          <stop offset="0" stop-color="#8cc63f"/>
          <stop offset="1" stop-color="#157a1c"/>
        </linearGradient>
      </defs>
      <path d="M0 252 Q250 220 526 280 L526 288 Q250 230 0 259 Z" fill="url(#band-green)"/>
      <path d="M0 259 Q250 232 526 288 L526 301 L0 301 Z" fill="url(#band-blue)"/>
    </svg>
    <p class="address">PO Box 140 Redgum Bay WA 6790</p>
  </section>

  <section class="card card--back-white" aria-label="Card back, white">
    <div class="brand brand--centered">
      <span class="brand__square"></span>
      <span class="brand__name">Vizo</span>
    </div>
    <p class="url">www.<span class="url__domain">vizo</span>.com.au</p>
  </section>

  <section class="card card--back-blue" aria-label="Card back, blue">
    <div class="brand brand--centered">
      <span class="brand__square"></span>
      <span class="brand__name">Vizo</span>
    </div>
    <p class="url">www.vizo.com.au</p>
  </section>

  <section class="card card--back-green" aria-label="Card back, green">
    <div class="brand brand--centered">
      <span class="brand__square"></span>
      <span class="brand__name">Vizo</span>
    </div>
    <p class="url">www.vizo.com.au</p>
  </section>
</body>
</html>
```